Form Crafters Business Card

Professional cosmetic surgery company, based in very exclusive area in London. High profiled clientele. Brand is very artistic, modern, state-of-the-art, safe. The best in the business. Celebrity clientele.

Form Crafter’s of London is a brand serving a discriminating and exclusive clientele who value personal service that is both intimate and high end. Our clients choose Form Crafters because of the relationships we share with all of our customers. The clients of Form Crafters have an equal partnership between customers, and very experienced, highly qualified medical professionals. This together provides you with a professional service that keeps you looking good and feeling good. It is a relationship based on honesty, compassion, loyalty and respect.
Form Crafter’s have provided services for internationally recognised celebrities, and other high profiled individuals.

The cards are used for networking at private, exclusive events with VIPs.

Target Market(s)

Professionals
Rich people

Industry/Entity Type

Professional Service

Contact Information for Business Card

Need double sided business card design for 4 people. Back of the business card needs to have contrast background to the front with butterfly watermark with services provided:
Hair Restoration surgery
Hair Loss treatments
Breast surgery
Rhinoplasty
Zelix Liposuction
Fat Grafting
Lumex & Fillers

Front of the business card needs to be a nice satin black.
with following information:
Talvan Desoruthy - name
Chief Executive - Job title

www.formcrafters-example.co.uk
talvan@formcrafters-example.co.uk
Phone: +44 (0)207 146 5327
Mobile: +44 (0)7491 825 436

The London Calder Infirmary
14 Pellmont Street | London | W1K 3TR
Off Dunmore Lane

All business cards have the same address, phone, website as Talvan's details.
Same details on the back of the business card as well.
The other cards have different name, job title, email, mobile number

Kerem Lutz - Name
Partner - Job Title
Former England International Cricketer - please include below job title

email: kerem@formcrafters-example.co.uk
mobile: +44(0)7862 514208

Dr Stellan Vastrel - Name
Plastic Surgeon - Job Title
drvastrel@formcrafters-example.co.uk
No mobile number

Dr Jon Torvick FRCS (please put FRCS in small font) - Name
Hair Restoration Surgeon - Job Title
drtorvick@formcrafters-example.co.uk
No mobile number

Colors
cedeec
85abd2
0655a3

Requirements
Must have
• The logo needs to be in a metallic finish
• Text needs to be striking
• nice background
• butterfly watermark on the back

```html
<!DOCTYPE html>
<html lang="en">
<head>
<meta charset="utf-8">
<title>Form Crafters Business Card</title>
<link rel="stylesheet" href="https://fonts.googleapis.com/css2?family=Lato:wght@400;700&display=swap">
<style>
  :root {
    --page: #e9eaec;
    --card: #2a2d31;
    --card-edge: #24272b;
    --blue: #1e8fd8;
    --blue-soft: #85abd2;
    --ink: #ffffff;
    --ink-muted: #d9dde2;
    --watermark: #3a3e43;
  }
  * { box-sizing: border-box; margin: 0; padding: 0; }
  html, body {
    width: 1000px; height: 1200px; overflow: hidden;
    background: var(--page);
    font-family: "Lato", sans-serif;
  }
  .sheet {
    width: 1000px; height: 1200px;
    display: flex; flex-direction: column; align-items: center;
    justify-content: center; gap: 60px;
  }
  .card {
    position: relative;
    width: 880px; height: 515px;
    background: linear-gradient(160deg, #2e3136 0%, var(--card) 55%, var(--card-edge) 100%);
    overflow: hidden;
    box-shadow: 0 2px 10px rgba(0,0,0,.18);
  }
  /* front */
  .watermark-area {
    position: absolute; left: 470px; top: 35px;
    width: 400px; height: 465px; display: block;
  }
  .holder { position: absolute; left: 104px; top: 100px; }
  .holder-name {
    font-size: 29px; font-weight: 700; letter-spacing: .3px;
    color: var(--ink); text-transform: uppercase; line-height: 1;
  }
  .holder-name .first { color: var(--blue); }
  .holder-name .last { font-weight: 400; }
  .holder-title { margin-top: 6px; font-size: 19px; color: var(--ink-muted); }
  .brand-name {
    position: absolute; font-family: "Lato", sans-serif;
    font-weight: 400; color: var(--blue); white-space: nowrap;
  }
  .front .brand-name { left: 104px; top: 232px; font-size: 40px; }
  .contact-list {
    position: absolute; left: 104px; top: 330px; list-style: none;
  }
  .contact-list li {
    display: flex; align-items: center; gap: 12px;
    font-size: 19px; color: var(--ink); height: 25.5px;
  }
  .contact-list svg { width: 16px; height: 16px; fill: var(--blue); flex: none; }
  /* back */
  .frame { position: absolute; left: 0; top: 0; width: 880px; height: 515px; }
  .back .brand-name {
    left: 0; width: 880px; text-align: center; top: 228px; font-size: 46px;
  }
</style>
</head>
<body>
<main class="sheet">

  <section class="card front" aria-label="Card front">
    <svg class="watermark-area" viewBox="0 0 400 465" role="img" aria-label="Faint brand watermark decoration">
      <defs>
        <radialGradient id="wm" cx="50%" cy="45%" r="60%">
          <stop offset="0" stop-color="#383c41"/>
          <stop offset="1" stop-color="#2b2e32" stop-opacity="0"/>
        </radialGradient>
      </defs>
      <rect width="400" height="465" fill="url(#wm)"/>
    </svg>

    <div class="holder">
      <p class="holder-name"><span class="first">Talvan</span> <span class="last">Desoruthy</span></p>
      <p class="holder-title">Chief Executive</p>
    </div>

    <p class="brand-name">Form Crafters</p>

    <ul class="contact-list">
      <li><svg viewBox="0 0 16 16"><path d="M8 1 1 7.5h2V15h4v-4h2v4h4V7.5h2z"/></svg>The London Calder Infirmary 14 Pellmont Street</li>
      <li><svg viewBox="0 0 16 16"><path d="M2 5c0-2 2-3 6-3s6 1 6 3v1h-3V4.5H5V6H2zm2 2h8l2 7H2z"/></svg>+44 (0)207 146 5327</li>
      <li><svg viewBox="0 0 16 16"><path d="M1 3h14v10H1zm1 1.2V5l6 4 6-4v-.8z"/></svg>talvan@formcrafters-example.co.uk</li>
      <li><svg viewBox="0 0 16 16"><circle cx="8" cy="8" r="7"/><path d="M1 8h14M8 1c3 3 3 11 0 14M8 1c-3 3-3 11 0 14" stroke="#2a2d31" stroke-width="1" fill="none"/></svg>www.formcrafters-example.co.uk</li>
    </ul>
  </section>

  <section class="card back" aria-label="Card back">
    <svg class="frame" viewBox="0 0 880 515" aria-hidden="true">
      <rect x="228" y="128" width="424" height="258" rx="34" fill="#26292d" stroke="var(--blue)" stroke-width="3"/>
      <rect x="214" y="114" width="452" height="286" rx="42" fill="none" stroke="var(--blue)" stroke-width="2" stroke-dasharray="9 6"/>
    </svg>
    <p class="brand-name">Form Crafters</p>
  </section>

</main>
</body>
</html>
```